Marco Bellin Photography needs a business card designs

I am looking for a business card with a logo clean and simple which I can use that logo on my website or on my pictures. It has to be very classy and very professional. Please look at my website at www.marcobphoto.com for my signature. I'm thinking of something like that for my signature/logo. I'm still working on my website but you get an idea. I'm open to any design but not too busy graphics.

I will be printing the business card from kelvaprint.com.

Surprise me :)

contact me if you have any questions.

-MB
Updates

I'm receiving a lot of black background at the moment. I know my website is all black doesn't mean I want my card to be all black. Please send in with some white background as well. Thanks :)

check out some business cards that I found online. I think they are simple and look really awesome. I don't want a card that is too busy.

http://www.marcobphoto.com/p270092084

Reason: Please extend the date for me. I haven't really receive any good design yet.

Industry/Entity Type

Printing

Requirements
Nice to have
• -a logo that related to my first and last initial of my name "MB"
-double sided
Should not have
• -I don't want my background to be all black.
-no pictures on the card

```html
<!DOCTYPE html>
<html lang="en">
<head>
<meta charset="utf-8">
<title>Marco Bellin Photography – Business Card</title>
<link href="https://fonts.googleapis.com/css2?family=PT+Sans:wght@400;700&family=Questrial&display=swap" rel="stylesheet">
<style>
  :root {
    --stage-green: #86c10f;
    --stage-green-edge: #74b000;
    --card-black: #050505;
    --card-sheen: #2c2c2c;
    --tab-white: #ffffff;
    --accent-red: #d8261f;
    --text-grey: #7a7a7a;
    --title-grey: #8e8e8e;
    --mark-dark: #2b2b2b;
    --mark-light: #c4c4c4;
    --label-white: #ffffff;
  }
  * { margin: 0; padding: 0; box-sizing: border-box; }
  html, body { width: 884px; height: 1200px; overflow: hidden; }
  body {
    position: relative;
    background: radial-gradient(ellipse at 50% 45%, var(--stage-green) 0%, var(--stage-green-edge) 100%);
    font-family: "PT Sans", Arial, sans-serif;
  }
  .card {
    position: absolute;
    left: 106px;
    width: 676px;
    height: 437px;
    overflow: hidden;
    background:
      radial-gradient(ellipse 70% 80% at 50% 0%, var(--card-sheen) 0%, var(--card-black) 75%);
  }
  .card--front { top: 125px; }
  .card--back { top: 661px; }

  .brand-tab {
    position: absolute;
    left: 61px;
    top: 0;
    width: 230px;
    height: 292px;
    background: var(--tab-white);
    border-radius: 0 0 30px 30px;
    display: flex;
    align-items: center;
    justify-content: center;
    gap: 10px;
    padding-top: 6px;
  }
  .brand-square {
    width: 14px;
    height: 14px;
    background: var(--accent-red);
    flex: none;
  }
  .brand-name {
    color: var(--mark-dark);
    font-weight: 700;
    font-size: 19px;
    line-height: 1.25;
    letter-spacing: 1px;
    text-transform: uppercase;
  }

  .person {
    position: absolute;
    left: 337px;
    top: 170px;
  }
  .person-name {
    color: var(--accent-red);
    font-weight: 700;
    font-size: 39px;
    line-height: 1;
    letter-spacing: 0.5px;
  }
  .person-role {
    margin-top: 6px;
    color: var(--title-grey);
    font-family: "Questrial", Arial, sans-serif;
    font-size: 19px;
    letter-spacing: 0.3px;
  }

  .contact {
    position: absolute;
    left: 0;
    right: 0;
    top: 358px;
    text-align: center;
    color: var(--text-grey);
    font-size: 15px;
    line-height: 22px;
  }
  .contact .sep { margin: 0 7px; }

  .back-brand {
    position: absolute;
    left: 0;
    right: 0;
    top: 0;
    bottom: 0;
    display: flex;
    align-items: center;
    justify-content: center;
    gap: 16px;
    padding-top: 40px;
  }
  .back-brand .brand-square { width: 22px; height: 22px; background: var(--mark-light); }
  .back-brand .brand-name {
    color: var(--mark-light);
    font-size: 34px;
    letter-spacing: 2px;
  }

  .side-label {
    position: absolute;
    left: 0;
    width: 884px;
    text-align: center;
    color: var(--label-white);
    font-family: Arial, Helvetica, sans-serif;
    font-size: 20px;
  }
  .side-label--front { top: 588px; }
  .side-label--back { top: 1119px; }
</style>
</head>
<body>
  <section class="card card--front">
    <div class="brand-tab">
      <span class="brand-square"></span>
      <span class="brand-name">Marco Bellin<br>Photography</span>
    </div>
    <div class="person">
      <p class="person-name">YOUR NAME</p>
      <p class="person-role">PHOTOGRAPHER</p>
    </div>
    <div class="contact">
      <p>website. www.yoursite.com<span class="sep">I</span>email. your_mail@yoursite.com</p>
      <p>mobile. 081 123 456 789<span class="sep">I</span>phone. 0123 456789<span class="sep">I</span>fax. 0123 456789</p>
    </div>
  </section>
  <p class="side-label side-label--front">FRONT</p>

  <section class="card card--back">
    <div class="back-brand">
      <span class="brand-square"></span>
      <span class="brand-name">Marco Bellin Photography</span>
    </div>
  </section>
  <p class="side-label side-label--back">BACK</p>
</body>
</html>
```